The website is called gearvorn.net. It's a DIY projects ( only mechanical engineering related projects ) where mechanical engineers/student can share their ideas/ DIY projects/tutorial/course projects/Graduation projects...etc.
The website is more or less like craftlumen.net ( please spend some time in this website ), but strictly to mechanical engineer and it will feature projects like pumps, turbines, compressor, gearboxes, automotive ...etc
There will be four categories:
1- Create, it's where the user can share his project, so it will have a writing feature ( title, body , upload image at different locations of the body ...etc)
2- Tutorials, where is user can share a tutorial so it should have a writing feature also
3- Build, where the user can see others projects
4- Buy, two items: a- T-shirts, b-Books ( DIY books made by us )
Notes:
-In the Share and tutorial categories, the user should select subcategory ( Will give them to you later ).
-When clicking to "make" category the user can see all the posted projects, then he can select a sub category ( see partwisp.net )
- each user will have a personal page
- Buy category will be added later if the website succeeded
- landing page feature the latest projects,tutorial
This is the full detail about the website, if there is something specific please let me know.
*No logo is been made yet.
thanks.
Industry/Entity Type
Mechanical Engineering

```html
<!DOCTYPE html>
<html lang="en">
<head>
<meta charset="utf-8">
<title>gearvorn.net — DIY Mechanical Projects</title>
<link rel="stylesheet" href="https://fonts.googleapis.com/css2?family=Oswald:wght@300;400&family=PT+Sans:wght@400;700&display=swap">
<style>
:root{
  --green:#8cc21c;
  --green-dark:#6fa312;
  --green-text:#7ab317;
  --ink:#555;
  --ink-soft:#666;
  --line:#dcdcdc;
  --topbar:#e4e4e4;
  --white:#fff;
}
*{box-sizing:border-box;margin:0;padding:0}
html,body{width:1163px;height:1200px;overflow:hidden;background:var(--white)}
body{position:relative;font-family:"PT Sans",sans-serif;color:var(--ink)}
.abs{position:absolute}
.cond{font-family:"Oswald",sans-serif;font-weight:400}

.topbar{left:0;top:0;width:1163px;height:38px;background:var(--topbar)}
.lang{left:746px;top:9px;width:79px;height:21px;background:#fff;border:1px solid #ccc;border-radius:2px;font-size:10px;line-height:19px;padding-left:26px;color:#444}
.lang .flag{position:absolute;left:7px;top:5px;width:14px;height:9px;background:#3a4f8f}
.lang svg{position:absolute;right:6px;top:7px}
.search{left:841px;top:9px;width:150px;height:21px;background:#fff;border:1px solid #d4d4d4;font-size:10px;font-style:italic;color:#aaa;line-height:19px;padding-left:7px}
.search svg{position:absolute;right:7px;top:5px}

.brand{left:181px;top:59px;display:flex;align-items:center;gap:10px}
.brand .mark{width:52px;height:52px;border-radius:50%;background:var(--green)}
.brand .name{font-family:"PT Sans",sans-serif;font-size:31px;color:var(--ink);font-weight:400}

.nav{left:496px;top:38px;height:92px;display:flex}
.nav a{display:block;height:92px;line-height:122px;font-family:"Oswald",sans-serif;font-size:13.5px;color:#555;text-decoration:none;padding:0 14px}
.nav a.active{background:linear-gradient(#fff 0%,#a6d43a 55%,var(--green) 100%);color:#fff}

.hero{left:0;top:130px;width:1163px;height:349px;background:linear-gradient(100deg,#1e1b17 0%,#4d4032 25%,#b28d4c 45%,#5a4b3a 65%,#6b5e52 80%,#c8401c 100%)}
.hero .arrow{position:absolute;top:142px}
.hero .caption{position:absolute;left:0;width:1163px;top:304px;text-align:center;color:#fff;font-family:"Oswald",sans-serif;font-size:19px;letter-spacing:-.6px;text-transform:uppercase}

.card{width:198px;height:94px;border:3px solid #e2e2e2;background:#fff;padding:5px 0 0 14px}
.card h3{font-family:"Oswald",sans-serif;font-weight:400;font-size:18px;color:var(--ink);line-height:24px}
.card p{font-size:10px;line-height:12.5px;color:var(--ink-soft);margin-top:2px;width:172px}
.btn{display:inline-block;margin-top:9px;height:21px;line-height:21px;padding:0 14px;background:linear-gradient(#9bd12c,var(--green-dark));color:#fff;font-size:10px;font-weight:700;border-radius:4px}

.section-title{font-family:"Oswald",sans-serif;font-weight:300;font-size:29px;color:var(--green-text);letter-spacing:-.5px}
.pager{left:705px;top:614px;display:flex;align-items:center;gap:6px;font-size:15px;color:#777}

.project{width:198px;height:177px;border:3px solid #e2e2e2;background:#fff}
.project .photo{height:116px}
.project h3{font-family:"Oswald",sans-serif;font-weight:400;font-size:18px;color:var(--ink);padding:1px 0 0 13px;line-height:24px}
.project p{font-size:10px;line-height:12.5px;color:var(--ink-soft);padding-left:14px;width:180px}

.cats{left:800px;top:647px;list-style:none}
.cats li{height:25.5px;line-height:16px;font-size:12px;color:#666;padding-left:16px;position:relative}
.cats li::before{content:"";position:absolute;left:0;top:4px;border-left:6px solid var(--green);border-top:4px solid transparent;border-bottom:4px solid transparent}

.footer{left:0;top:1037px;width:1163px;height:163px;background:linear-gradient(var(--green),#8fc41f)}
.newsletter{left:173px;top:1066px;width:221px;height:99px;background:#f5f5f5;border:4px solid #d9d9d9;padding:8px 0 0 14px}
.newsletter h4{font-size:14px;color:#777;font-weight:700;letter-spacing:.3px}
.newsletter .field{margin-top:5px;width:189px;height:21px;border:1px solid #ccc;background:#fff;font-size:10px;color:#999;line-height:19px;padding-left:8px;position:relative}
.newsletter .field span{position:absolute;right:-1px;top:-1px;height:21px;line-height:21px;padding:0 9px;background:#e32222;color:#fff;font-weight:700;border-radius:3px}
.newsletter p{font-size:10px;color:#666;line-height:12px;margin-top:5px}
.fcol h5{font-size:12px;color:#fff;font-weight:700}
.fcol a,.fcol p{display:block;font-size:11px;color:#fff;text-decoration:none}
.social{left:780px;top:1096px;display:flex;gap:6px}
.social span{width:27px;height:27px;border-radius:50%;background:#fff;border:2px solid #e8f3d2;display:block}
.legal{left:782px;top:1138px;font-size:11px;color:#fff;line-height:19px}
</style>
</head>
<body>

<div class="abs topbar"></div>
<div class="abs lang"><span class="flag"></span>English
  <svg width="7" height="5" viewBox="0 0 7 5"><path d="M0 0 L3.5 4 L7 0" fill="none" stroke="#333" stroke-width="1.4"/></svg></div>
<div class="abs search">Search
  <svg width="10" height="10" viewBox="0 0 10 10"><circle cx="4" cy="4" r="3" fill="none" stroke="#aaa" stroke-width="1.2"/><path d="M6 6 L9 9" stroke="#aaa" stroke-width="1.4"/></svg></div>

<div class="abs brand"><span class="mark"></span><span class="name">Gearvorn</span></div>

<nav class="abs nav">
  <a class="active">HOME</a><a>SERVICES</a><a>PROJECTS</a><a>EXPERTS</a><a>TUTORIALS</a><a>BLOG</a><a>CONTACT US</a>
</nav>

<section class="abs hero" role="img" aria-label="Cutaway photograph of a car gearbox with brass gears and shafts">
  <svg class="arrow" style="left:174px" width="32" height="70" viewBox="0 0 32 70"><path d="M28 0 L4 35 L28 70" fill="none" stroke="#ddd" stroke-width="8" opacity=".85"/></svg>
  <svg class="arrow" style="left:958px" width="32" height="70" viewBox="0 0 32 70"><path d="M4 0 L28 35 L4 70" fill="none" stroke="#ddd" stroke-width="8" opacity=".85"/></svg>
  <div class="caption">We are a DIY - Do it yourself mechanical projects collection online for engineering students.</div>
</section>

<div class="abs card" style="left:171px;top:493px"><h3>Create</h3><p>Lorem ipsum dolor sit , consectetuer adipiscing elit.</p><span class="btn">Create or Share Project</span></div>
<div class="abs card" style="left:380px;top:493px"><h3>Tutorials</h3><p>Lorem ipsum dolor sit , consectetuer adipiscing elit.</p><span class="btn">Upload Project</span></div>
<div class="abs card" style="left:587px;top:493px"><h3>Build</h3><p>Lorem ipsum dolor sit , consectetuer adipiscing elit.</p><span class="btn">View Project</span></div>
<div class="abs card" style="left:793px;top:493px"><h3>Buy</h3><p>Lorem ipsum dolor sit , consectetuer adipiscing elit.</p><span class="btn">Buy Now</span></div>

<h2 class="abs section-title" style="left:171px;top:598px">Recent Projects</h2>
<div class="abs pager">
  <svg width="8" height="11" viewBox="0 0 8 11"><path d="M8 0 L0 5.5 L8 11Z" fill="var(--green)"/></svg>
  <span>1</span><span>2</span><span>3</span>
  <svg width="8" height="11" viewBox="0 0 8 11"><path d="M0 0 L8 5.5 L0 11Z" fill="var(--green)"/></svg>
</div>
<h2 class="abs section-title" style="left:796px;top:598px">Projects Categories</h2>

<div class="abs project" style="left:171px;top:651px"><div class="photo" role="img" aria-label="Close-up of a magnifying glass over a small circuit board" style="background:linear-gradient(135deg,#8a5a48,#3b5f8e 60%,#c99b80)"></div><h3>Create</h3><p>Lorem ipsum dolor sit , consectetuer adipiscing elit.</p></div>
<div class="abs project" style="left:380px;top:651px"><div class="photo" role="img" aria-label="Technician working at a metal machining station" style="background:linear-gradient(90deg,#c8ccd0,#6d7378 55%,#1f6fb5)"></div><h3>Create</h3><p>Lorem ipsum dolor sit , consectetuer adipiscing elit.</p></div>
<div class="abs project" style="left:587px;top:651px"><div class="photo" role="img" aria-label="Toy crane model with a large gear" style="background:linear-gradient(120deg,#e8e8e8,#9a9a9a 55%,#e4c23a)"></div><h3>Create</h3><p>Lorem ipsum dolor sit , consectetuer adipiscing elit.</p></div>
<div class="abs project" style="left:171px;top:842px"><div class="photo" role="img" aria-label="Small robot chassis with motors and wiring" style="background:linear-gradient(135deg,#d4d4d4,#5a5048 55%,#b9b9b9)"></div><h3>Create</h3><p>Lorem ipsum dolor sit , consectetuer adipiscing elit.</p></div>
<div class="abs project" style="left:380px;top:842px"><div class="photo" role="img" aria-label="Stainless steel centrifugal pump housing" style="background:linear-gradient(135deg,#f2f2f2,#9ea4aa 50%,#dfe2e5)"></div><h3>Create</h3><p>Lorem ipsum dolor sit , consectetuer adipiscing elit.</p></div>
<div class="abs project" style="left:587px;top:842px"><div class="photo" role="img" aria-label="Engine block with pulleys and belts" style="background:linear-gradient(135deg,#3c3c3c,#9a9a9a 55%,#4a4a4a)"></div><h3>Create</h3><p>Lorem ipsum dolor sit , consectetuer adipiscing elit.</p></div>

<ul class="abs cats">
  <li>Lorem ipsum dolor sit</li><li>Consectetuer adipiscing</li><li>Aenean commodo</li>
  <li>Lorem ipsum dolor sit</li><li>Consectetuer adipiscing</li><li>Aenean commodo</li>
  <li>Lorem ipsum dolor sit</li><li>Consectetuer adipiscing</li><li>Aenean commodo</li>
  <li>Lorem ipsum dolor sit</li><li>Consectetuer adipiscing</li><li>Aenean commodo</li>
  <li>Lorem ipsum dolor sit</li><li>Consectetuer adipiscing</li><li>Aenean commodo</li>
</ul>

<footer class="abs footer"></footer>
<div class="abs newsletter">
  <h4>Join Our Newsletter</h4>
  <div class="field">Enter Your Email Address<span>Sign Up</span></div>
  <p>Signup to receive invite to special events, parties, cooking demos, coupons</p>
</div>
<div class="abs fcol" style="left:443px;top:1064px">
  <h5>Company</h5>
  <a style="margin-top:19px">Privacy</a><a style="margin-top:6px">Terms Of Use</a><a style="margin-top:6px">Terms Of Trade</a><a style="margin-top:6px">PO T&amp;C's</a>
</div>
<div class="abs fcol" style="left:579px;top:1064px;width:160px">
  <h5>Twitter Update</h5>
  <p style="margin-top:19px;line-height:16px">&nbsp;@lathebright there is a new designer in town people!</p>
  <p style="margin-top:15px">Check it out: http://lnk.gvr</p>
</div>
<div class="abs fcol" style="left:779px;top:1064px"><h5>Follow Us Online</h5></div>
<div class="abs social"><span></span><span></span><span></span><span></span></div>
<div class="abs legal">Privacy Policy | Terms of Services | Sitemap<br>Copyright © 2013. All Rights Reserved.</div>

</body>
</html>
```